Pondmentor: an app for coaches and students in golf and fitness

I currently have an app that is called Pondmentor and I am redoing the app completely and with this I am looking for a cool design for the app. I am not happy with the design as it is at the moment. The app should have a nice welcome and when you are logged in the dashboard must be very modern. It is a golf app that have 2 type of users. 1 user is the coach and the other user is the student. Those users can see different things of course.
The coach is normally paying a subscription charge for using the app but I want to get the students to pay for different tools that I will be offering via the app. To me the dashboard and the homepage of the app (once you have downloaded the app) is important. Here I would like to get the student as well as the coach the feeling of what the app can offer. The app offers features like Calendar (here the student can book the coach via the calendar), Chat (here the coach and the student can chat with each other as well as the coach can creat group chats with several students), Notes (here the coach as well as the student can create notes for their lessons), video tips (here the coach can upload video tips for his/her students, online lesson (the student can take online lessons by uploading recorded videos..and so on

Target Market(s)

Sport coaches (for start it will be mostly golf coaches)

Industry/Entity Type

Sports

Font styles to use
Sans Serif

Colors
0054AA
0677BA
7BADD7
CADEEF
E8F1F8

Requirements
Must have
• modern design and easy navigation.
Nice to have
• It all starts with the dashboard
Should not have
• boring standard style.

```html
<!DOCTYPE html>
<html lang="en">
<head>
<meta charset="utf-8">
<title>Pondmentor – Welcome and Dashboard</title>
<link rel="stylesheet" href="https://fonts.googleapis.com/css2?family=Poppins:wght@300;400;600;700&display=swap">
<style>
  :root{
    --page:#f1f3f3;
    --deep:#1f5269;
    --ink:#0d4a66;
    --brand:#0677ba;
    --sky:#7badd7;
    --mist:#cadeef;
    --frost:#e8f1f8;
    --glass:rgba(232,241,248,.28);
    --glass-grey:rgba(190,200,205,.42);
    --white:#ffffff;
  }
  *{box-sizing:border-box;margin:0;padding:0}
  html,body{width:1200px;height:1183px;overflow:hidden;background:var(--page);font-family:"Poppins",sans-serif}
  .canvas{position:relative;width:1200px;height:1183px}
  .screen{position:absolute;top:158px;width:400px;height:866px;border-radius:46px;overflow:hidden}
  .screen--welcome{left:150px}
  .screen--dashboard{left:650px}

  .backdrop{position:absolute;inset:0}
  .screen--welcome .backdrop{
    background:
      radial-gradient(circle at 28% 62%, #6fb3d6 0 46px, transparent 60px),
      linear-gradient(160deg,#3f7d97 0%,#2d5d73 45%,#3b7f9e 75%,#4a91b2 100%);
  }
  .screen--dashboard .backdrop{
    background:
      radial-gradient(circle at 72% 10%, #8fd0ee 0 70px, transparent 150px),
      radial-gradient(circle at 40% 70%, #6fb3d6 0 40px, transparent 70px),
      linear-gradient(165deg,#6ab9dd 0%,#3f8fb4 35%,#2f6a85 70%,#3d85a7 100%);
  }

  /* Welcome */
  .welcome-panel{position:absolute;top:0;right:0;width:330px;height:520px;background:rgba(216,232,240,.82);border-bottom-left-radius:90px;border-top-left-radius:90px}
  .brand{position:absolute;top:170px;left:0;right:0;text-align:center}
  .brand__mark{display:inline-flex;align-items:center;gap:8px}
  .brand__dot{width:16px;height:16px;border-radius:50%;background:var(--brand)}
  .brand__name{font-size:30px;font-weight:700;color:var(--ink);letter-spacing:-.5px}
  .brand__tagline{margin-top:16px;font-size:22px;font-weight:300;color:var(--sky)}
  .brand__sub{margin-top:6px;font-size:14px;font-weight:400;color:var(--ink)}
  .cta{position:absolute;left:40px;bottom:110px;width:150px;height:48px;border-radius:12px;background:rgba(232,241,248,.18);border:1px solid rgba(232,241,248,.3);color:var(--white);font:400 15px "Poppins",sans-serif;display:flex;align-items:center;justify-content:center}

  /* Dashboard */
  .greeting{position:absolute;top:64px;left:28px;display:flex;align-items:center;gap:14px}
  .avatar{width:56px;height:56px;border-radius:14px;background:linear-gradient(135deg,#c96f5a,#7e9a78)}
  .greeting__label{font-size:13px;font-weight:600;color:var(--white)}
  .greeting__name{font-size:22px;font-weight:300;color:var(--white);line-height:1.1}
  .tiles{position:absolute;top:150px;left:24px;right:24px}
  .tile{position:absolute;width:168px;height:168px;border-radius:20px;background:var(--glass);border:1px solid rgba(255,255,255,.25);padding:18px 16px;color:var(--white);display:flex;flex-direction:column;align-items:center;text-align:center}
  .tile--grey{background:var(--glass-grey)}
  .tile svg{width:52px;height:52px;margin-bottom:10px;fill:none;stroke:var(--white);stroke-width:2.6;stroke-linecap:round;stroke-linejoin:round}
  .tile__title{font-size:14px;font-weight:600}
  .tile__text{font-size:10px;font-weight:300;line-height:1.35;margin-top:4px}
  .tile--calendar{left:184px;top:0}
  .tile--products{left:0;top:96px}
  .tile--lessons{left:184px;top:184px}
  .tile--offers{left:0;top:280px}
  .tile--students{left:184px;top:368px}
  .tile--pond{left:0;top:464px}
</style>
</head>
<body>
<div class="canvas">

  <section class="screen screen--welcome">
    <div class="backdrop" role="img" aria-label="Blurred photo of a golf ball on a tee with a club behind it"></div>
    <div class="welcome-panel"></div>
    <div class="brand">
      <div class="brand__mark"><span class="brand__dot"></span><span class="brand__name">Pondmentor</span></div>
      <p class="brand__tagline">Improve your training</p>
      <p class="brand__sub">...on and off the course</p>
    </div>
    <div class="cta">Get started</div>
  </section>

  <section class="screen screen--dashboard">
    <div class="backdrop" role="img" aria-label="Blurred photo of a golf ball on a green course"></div>
    <header class="greeting">
      <div class="avatar" role="img" aria-label="Coach profile photo"></div>
      <div>
        <p class="greeting__label">Welcome</p>
        <p class="greeting__name">Lena Marsh</p>
      </div>
    </header>
    <div class="tiles">
      <article class="tile tile--calendar">
        <svg viewBox="0 0 52 52"><rect x="6" y="9" width="40" height="37" rx="9"/><path d="M16 5v8M36 5v8M15 22h22M15 30h22M15 38h12"/></svg>
        <h3 class="tile__title">My Calendar</h3>
        <p class="tile__text">Book and manage your appointment 24/7</p>
      </article>
      <article class="tile tile--products tile--grey">
        <svg viewBox="0 0 52 52"><rect x="6" y="6" width="40" height="40" rx="10"/><path d="M16 18h20M16 26h20M16 34h12"/></svg>
        <h3 class="tile__title">My Products</h3>
        <p class="tile__text">Configure lessions details for calendar and online lessons</p>
      </article>
      <article class="tile tile--lessons">
        <svg viewBox="0 0 52 52"><path d="M6 14a6 6 0 0 1 6-6h10l5 6h13a6 6 0 0 1 6 6v18a6 6 0 0 1-6 6H12a6 6 0 0 1-6-6z"/></svg>
        <h3 class="tile__title">Online Lessons</h3>
        <p class="tile__text">Edit and view your students online lessons</p>
      </article>
      <article class="tile tile--offers">
        <svg viewBox="0 0 52 52"><rect x="8" y="10" width="36" height="34" rx="4"/><path d="M8 18h36M14 10v8M22 10v8M30 10v8M38 10v8M18 26h16v12H18z"/></svg>
        <h3 class="tile__title">My Offers</h3>
        <p class="tile__text">Here pro can offer provide info to students</p>
      </article>
      <article class="tile tile--students tile--grey">
        <svg viewBox="0 0 52 52"><circle cx="34" cy="14" r="7"/><ellipse cx="20" cy="34" rx="9" ry="13"/></svg>
        <h3 class="tile__title">My Students</h3>
        <p class="tile__text">Fina all infomation of your student</p>
      </article>
      <article class="tile tile--pond">
        <svg viewBox="0 0 52 52"><path d="M8 22h8l14-8v24l-14-8H8z"/><path d="M36 20l6-4M36 26h8M36 32l6 4"/></svg>
        <h3 class="tile__title">Pond365</h3>
        <p class="tile__text">Here pro can offer provide info to students</p>
      </article>
    </div>
  </section>

</div>
</body>
</html>
```